Vesk Architecture

We are a architectural design and build company working between scales 1/1000 to 1/1 we want people to understand our difference from our design experience and quality.we build hotels restourants and office spaces.Our company name is Vesk architecture to mind sustainability.

We want to write our adress phone and work spesifications on the card and we want our logo as backround.

Ps:you could find the logo adress and phone box numbers from the web:www.veskmimarlik-ornek.com

Target Market(s)

Who looks for experts.

Industry/Entity Type

Architecture

Requirements
Must have
• Design is over everything.
Should not have
• we don want it to be colorfull

```html
<!DOCTYPE html>
<html lang="tr">
<head>
<meta charset="utf-8">
<title>Vesk Mimarlık – Business Cards</title>
<link rel="stylesheet" href="https://fonts.googleapis.com/css2?family=Questrial&display=swap">
<style>
  :root {
    --canvas: #ffffff;
    --cream: #e9e5a8;
    --charcoal: #282b2d;
    --ink: #2a2c2e;
    --band-light-a: rgba(120, 118, 80, 0.05);
    --band-light-b: rgba(120, 118, 80, 0.16);
    --band-dark-a: rgba(106, 109, 107, 0.10);
    --band-dark-b: rgba(106, 109, 107, 0.38);
    --web-grey: #8d908f;
  }
  html, body {
    margin: 0;
    padding: 0;
    overflow: hidden;
    background: var(--canvas);
  }
  .canvas {
    position: relative;
    width: 1200px;
    height: 1200px;
    background: var(--canvas);
    font-family: "Questrial", sans-serif;
    overflow: hidden;
  }
  .card {
    position: absolute;
    top: 250px;
    width: 440px;
    height: 690px;
    border-radius: 28px;
    overflow: hidden;
    box-shadow: 0 10px 24px rgba(0, 0, 0, 0.18);
  }
  .card--front { left: 120px; background: var(--cream); color: var(--ink); }
  .card--back  { left: 640px; background: var(--charcoal); }

  .band {
    position: absolute;
    width: 180px;
  }
  .card--front .band {
    left: 148px;
    background: linear-gradient(180deg, var(--band-light-b), var(--band-light-a));
  }
  .card--front .band--top    { top: 0; height: 150px; }
  .card--front .band--bottom { top: 262px; bottom: 0; }
  .card--back .band {
    left: 130px;
    background: linear-gradient(180deg, var(--band-dark-b), var(--band-dark-a));
  }
  .card--back .band--top    { top: 0; height: 280px; }
  .card--back .band--bottom { top: 400px; height: 200px; }

  .wordmark {
    position: absolute;
    left: 0;
    right: 0;
    text-align: center;
    font-size: 54px;
    letter-spacing: 2px;
    line-height: 1;
    text-transform: lowercase;
  }
  .card--front .wordmark { top: 170px; color: var(--ink); padding-left: 30px; }
  .card--back  .wordmark { top: 300px; color: var(--cream); }
  .wordmark-sub {
    display: block;
    font-size: 20px;
    letter-spacing: 3px;
    margin-top: 12px;
    text-transform: uppercase;
  }
  .holder {
    position: absolute;
    left: 92px;
    top: 378px;
  }
  .holder-name { font-size: 21px; margin: 0; }
  .holder-role { font-size: 17px; margin: 8px 0 0; }
  .holder-fields { font-size: 13px; margin: 8px 0 0; letter-spacing: 0.4px; }
  .contact {
    position: absolute;
    left: 92px;
    top: 480px;
    margin: 0;
    padding: 0;
    list-style: none;
    font-size: 13.5px;
    line-height: 30px;
    letter-spacing: 0.3px;
  }
  .website {
    position: absolute;
    bottom: 48px;
    left: 0;
    right: 0;
    text-align: center;
    color: var(--web-grey);
    font-size: 15px;
    letter-spacing: 1.5px;
  }
</style>
</head>
<body>
<main class="canvas">

  <section class="card card--front" aria-label="Business card front">
    <div class="band band--top" role="img" aria-label="Decorative vertical line pattern"></div>
    <div class="band band--bottom" role="img" aria-label="Decorative vertical line pattern"></div>
    <div class="wordmark">vesk<span class="wordmark-sub">Mimarlık</span></div>
    <div class="holder">
      <p class="holder-name">Deniz Arman YALCIN</p>
      <p class="holder-role">Mimar</p>
      <p class="holder-fields">Otel · Restoran · Ofis</p>
    </div>
    <ul class="contact">
      <li>Ornek Mah. Liman Cad. Defne Sok.</li>
      <li>No : 7 Kadiköy / ISTANBUL</li>
      <li>Tel : 0216 555 41 20</li>
      <li>Fax : 0216 555 41 21</li>
      <li>Email: vesk@ornekposta.com</li>
    </ul>
  </section>

  <section class="card card--back" aria-label="Business card back">
    <div class="band band--top" role="img" aria-label="Decorative vertical line pattern"></div>
    <div class="band band--bottom" role="img" aria-label="Decorative vertical line pattern"></div>
    <div class="wordmark">vesk<span class="wordmark-sub">Mimarlık</span></div>
    <div class="website">www.veskmimarlik-ornek.com</div>
  </section>

</main>
</body>
</html>
```